Tranquilly Balanced Restoration

We want to design a business card that is modern and appealing for an innovative psychedelic telemedicine company that provides at-home ketamine-assisted therapy along with wellness, longevity, and anti-aging medicines. We want to use our deep purple and white plus other colors you can find on our website. We don't have any strict brand guidelines yet so feel free to get creative. We want a very professional, but technology first modern design that will instill trust, peace, calm, but also be attractive to investors in the healthcare and SaaS space.

```html
<!DOCTYPE html>
<html lang="en">
<head>
<meta charset="utf-8">
<title>Tranquilly Balanced Restoration — Business Card</title>
<link href="https://fonts.googleapis.com/css2?family=Poppins:wght@400;500;600&display=swap" rel="stylesheet">
<style>
  :root {
    --purple: #7d69aa;
    --purple-deep: #6a5698;
    --purple-text: #6b559c;
    --orchid: #b06aa0;
    --white: #ffffff;
    --backdrop: #ecebf0;
  }
  * { margin: 0; padding: 0; box-sizing: border-box; }
  html, body {
    width: 1200px; height: 900px; overflow: hidden;
    background: var(--backdrop);
    font-family: "Poppins", sans-serif;
  }
  .card {
    position: absolute; left: 250px; width: 700px; height: 400px;
    overflow: hidden;
    box-shadow: 0 6px 18px rgba(40, 30, 70, 0.18);
  }
  .card-front { top: 40px; background: var(--purple); }
  .card-back { top: 470px; background: var(--white); }

  .front-brand {
    position: absolute; inset: 0;
    display: flex; flex-direction: column; align-items: center; justify-content: center; gap: 22px;
  }
  .front-brand .brand-dot {
    width: 70px; height: 70px; border-radius: 50%;
    background: var(--purple-deep);
  }
  .front-brand .brand-name {
    font-weight: 400; font-size: 64px; letter-spacing: 1px;
    color: var(--purple-deep);
  }

  .back-wave { position: absolute; left: 0; top: 0; width: 700px; height: 400px; }

  .person { position: absolute; left: 50px; top: 48px; }
  .person-name { font-weight: 600; font-size: 32px; color: var(--orchid); line-height: 1.1; }
  .person-role { font-weight: 400; font-size: 17px; color: var(--purple-text); }

  .contact { position: absolute; left: 50px; top: 170px; color: var(--purple-text); font-size: 18px; line-height: 1.45; }
  .contact-row { display: flex; align-items: center; gap: 10px; }
  .contact-row svg { width: 20px; height: 20px; flex: none; }
  .contact-address { margin-top: 12px; padding-left: 30px; }

  .back-brand {
    position: absolute; right: 50px; top: 40px;
    display: flex; flex-direction: column; align-items: center; gap: 10px;
  }
  .back-brand .brand-dot {
    width: 50px; height: 50px; border-radius: 50%;
    background: var(--purple);
  }
  .back-brand .brand-name { font-weight: 400; font-size: 38px; line-height: 1.2; color: var(--orchid); }

  .website {
    position: absolute; right: 40px; bottom: 38px;
    color: var(--white); font-size: 17px; letter-spacing: 0.5px;
  }
</style>
</head>
<body>

<section class="card card-front" aria-label="Card front">
  <div class="front-brand">
    <span class="brand-dot"></span>
    <span class="brand-name">Tranquilly</span>
  </div>
</section>

<section class="card card-back" aria-label="Card back">
  <svg class="back-wave" viewBox="0 0 700 400" aria-hidden="true">
    <path d="M0,318 C180,322 340,296 490,242 C380,302 210,338 0,340 Z" fill="var(--orchid)"/>
    <path d="M0,348 C200,344 380,308 500,264 C580,234 640,214 700,202 L700,400 L0,400 Z" fill="var(--purple)"/>
  </svg>

  <div class="person">
    <p class="person-name">Daniel Mercer</p>
    <p class="person-role">Managing Director</p>
  </div>

  <div class="contact">
    <p class="contact-row">
      <svg viewBox="0 0 24 24" aria-hidden="true"><path fill="var(--orchid)" d="M6.6 10.8a15.1 15.1 0 0 0 6.6 6.6l2.2-2.2c.3-.3.7-.4 1-.2 1.1.4 2.3.6 3.6.6.6 0 1 .4 1 1V20c0 .6-.4 1-1 1A17 17 0 0 1 3 4c0-.6.4-1 1-1h3.5c.6 0 1 .4 1 1 0 1.3.2 2.5.6 3.6.1.3 0 .7-.2 1z"/></svg>
      <span>044-555 018 274</span>
    </p>
    <p class="contact-row">
      <svg viewBox="0 0 24 24" aria-hidden="true"><rect x="2" y="5" width="20" height="14" fill="var(--orchid)"/><path d="M2 5l10 8 10-8" fill="none" stroke="var(--white)" stroke-width="1.6"/></svg>
      <span>care@tranquillyrx.com</span>
    </p>
    <p class="contact-address">88 Willow Crest Lane<br>Lakeview, 60614</p>
  </div>

  <div class="back-brand">
    <span class="brand-dot"></span>
    <span class="brand-name">Tranquilly</span>
  </div>

  <p class="website">www.tranquillyrx.com</p>
</section>

</body>
</html>
```